Create a 2-sided postcard design (standard size) for Torlen Systems, a professional low-voltage and security integration company.
Side 1 – Front (Marketing Side)
Headline / Intro:
"Torlen Systems – Security, Connectivity, and Peace of Mind."
Brief Overview / Summary:
Torlen Systems provides complete security and technology integration solutions for commercial, industrial, and multifamily properties. From access control to fire systems, we specialize in delivering seamless, scalable, and reliable installations supported by professional service and ongoing care.
Services Breakdown:
Access Control – Cloud-based and enterprise access solutions to manage entry and permissions.
CCTV / Video Surveillance – Protect your property with high-definition cameras and remote monitoring.
Intrusion Alarm – Professional-grade systems to detect and deter unauthorized access.
Audio-Visual – From conference rooms to distributed audio and digital displays.
Fire Systems – Code-compliant alarm systems with 24/7 QX monitoring and life-safety support.
Structured Data Cabling – Low-voltage and fiber cabling for reliable network infrastructure.
Trusted By (Logos):
Moro, Velpurna, Gildpath, Carrow Investments, Bolt Hardware, Quillfen Games, Ledger Stewardship Partners, KEYframe
Technology partners:
Include logos of brands like Tamzo, Rook Lantern Networks, JMW , Digital Sentrel, Polmira, RTN, Blazeron
Contact Info:
📧 sales@torlensystems.example
📞 555-014-2739
🌐 torlensystems.example
🖼️ Side 2 – Back (Branding Side)
Primary Focus:
Large, centered Torlen Systems logo.
Subtext / Tagline (Optional):
“Your Security and Technology Partner.”
List of Services (Under Logo):
Access Control | CCTV | Intrusion Alarm | Audio-Visual | Fire | Data
🎨 Design Preferences:
Clean, modern, and professional layout.
Corporate tones (e.g., black and white, bold accents).
Use clean typography and icons for service areas.
Logo should be prominent on the back and represent the brand with strength and clarity.
Open to designer layout and creative interpretation as long as it stays on brand.
Industry/Entity Type
Commercial Security
Colors
Designer to choose only greyscale colors for use in the design.
Look and feel
Each slider illustrates characteristics of the customer's brand and the style your logo design should communicate.

```html
<!DOCTYPE html>
<html lang="en">
<head>
<meta charset="utf-8">
<title>Torlen Systems – Postcard Front</title>
<link href="https://fonts.googleapis.com/css2?family=Poppins:wght@300;400;500;600;700&display=swap" rel="stylesheet">
<style>
:root{
  --stage:#d6d6d6;
  --navy:#1c2b3b;
  --panel:#0c1f31;
  --accent:#3ba6d8;
  --accent-soft:#cfe6f1;
  --ink:#111820;
  --white:#ffffff;
  --divider:#2a4a63;
}
*{box-sizing:border-box;margin:0;padding:0}
html,body{width:897px;height:1200px;overflow:hidden;background:var(--stage);font-family:'Poppins',sans-serif}
.postcard{position:absolute;left:48px;top:0;width:1200px;height:1800px;transform:scale(.6667);transform-origin:0 0;background:var(--navy);overflow:hidden}
.abs{position:absolute}
.nowrap{white-space:nowrap}

.hero-art{left:0;top:0}
.brand{left:60px;top:52px;color:var(--ink)}
.brand-name{font-size:74px;font-weight:700;line-height:1;letter-spacing:-1px}
.brand-sub{font-size:36px;font-weight:500;letter-spacing:13px;margin-top:4px}
.accent-bar{left:0;top:218px;width:53px;height:17px;background:var(--accent)}
.headline{left:77px;top:202px;font-size:46px;line-height:60px;color:var(--ink);font-weight:400;white-space:nowrap}
.headline .lead{color:var(--accent);font-weight:500;font-size:48px}

.shield-art{left:85px;top:590px;width:340px;height:340px;border-radius:50%;background:radial-gradient(circle at 45% 45%,#d9f1fb 0%,#6cc0e6 22%,#2a5d80 48%,rgba(28,43,59,0) 70%)}

.tag{border:3px solid var(--accent);border-radius:12px;color:var(--accent-soft);font-size:40px;font-weight:300;text-align:center;line-height:54px;background:var(--navy)}
.tag-overview{left:624px;top:617px;width:318px;height:60px}
.overview-rule{left:472px;top:702px;width:3px;height:196px;background:var(--accent)}
.overview-text{left:522px;top:697px;font-size:24px;line-height:32.5px;color:var(--white);font-weight:300;white-space:nowrap}

.services-panel{left:32px;top:992px;width:1138px;height:520px;border-radius:14px;background:linear-gradient(180deg,#0b1d2e,#0f2539)}
.tag-services{left:466px;top:963px;width:317px;height:60px;background:var(--panel)}
.service-icon{width:80px;height:80px;stroke:var(--accent);fill:none;stroke-width:2.5}
.service{color:var(--white);font-size:22px;line-height:30px;font-weight:300;white-space:nowrap}
.service h3{color:var(--accent);font-size:21px;font-weight:300;line-height:28px;margin-bottom:4px}
.divider{width:2px;background:var(--divider)}

.trusted{left:36px;top:1543px;width:1060px;height:67px;background:var(--white);display:flex;align-items:center;justify-content:space-between;padding:0 24px 0 14px}
.trusted-tail{left:1060px;top:1543px}
.trusted .label{font-size:23px;color:var(--ink);white-space:nowrap}
.trusted .mark{font-size:19px;font-weight:600;color:var(--navy);white-space:nowrap;display:flex;align-items:center;gap:6px}
.dot{width:12px;height:12px;background:var(--accent);border-radius:50%;display:inline-block}

.tech-bar{left:0;top:1647px;width:46px;height:16px;background:var(--accent)}
.tech-label{left:62px;top:1643px;font-size:23px;line-height:30px;color:var(--white);font-weight:300}
.partner{top:1648px;height:54px;background:var(--white);display:flex;align-items:center;justify-content:center;font-size:16px;font-weight:600;color:var(--navy);text-align:center;line-height:18px}

.footer{left:0;top:1720px;width:1200px;height:80px;background:linear-gradient(90deg,#2d3d4d,#000 75%)}
.footer-brand{left:28px;top:1732px;color:var(--white)}
.footer-brand .brand-name{font-size:38px;letter-spacing:0}
.footer-brand .brand-sub{font-size:17px;letter-spacing:7px;margin-top:0}
.contact{top:1747px;font-size:20px;color:var(--white);display:flex;align-items:center;gap:10px;font-weight:300;white-space:nowrap}
.contact svg{width:26px;height:26px;stroke:var(--accent);fill:none;stroke-width:2}
.phone-box{left:835px;top:1738px}
.phone{left:893px;top:1745px;font-size:35px;color:var(--white);display:flex;align-items:center;gap:14px;font-weight:300;white-space:nowrap}
.phone svg{width:30px;height:30px;fill:var(--white)}
</style>
</head>
<body>
<main class="postcard">
  <svg class="abs hero-art" width="1200" height="580" viewBox="0 0 1200 580">
    <defs>
      <linearGradient id="heroSky" x1="0" y1="0" x2="1" y2="0">
        <stop offset="0" stop-color="#ffffff"/><stop offset=".5" stop-color="#f3f9fc"/><stop offset="1" stop-color="#cfe6f1"/>
      </linearGradient>
      <linearGradient id="heroPhoto" x1="0" y1="0" x2="1" y2="1">
        <stop offset="0" stop-color="#f3f9fc" stop-opacity="0"/><stop offset=".45" stop-color="#c9e4f0"/><stop offset="1" stop-color="#86bdd6"/>
      </linearGradient>
    </defs>
    <polygon points="0,0 1200,0 1200,485 835,572 0,375" fill="url(#heroSky)"/>
    <polygon role="img" aria-label="Photo of a technician holding a transparent tablet, with faint hexagon tech graphics" points="560,0 1200,0 1200,485 835,572 560,508" fill="url(#heroPhoto)"/>
  </svg>

  <div class="abs brand"><div class="brand-name">TORLEN</div><div class="brand-sub">SYSTEMS</div></div>
  <div class="abs accent-bar"></div>
  <h1 class="abs headline"><span class="lead">TORLEN SYSTEMS</span><br>SECURITY, CONNECTIVITY,<br>AND PEACE OF MIND</h1>

  <div class="abs shield-art" role="img" aria-label="Glowing security shield illustration with a tick and orbit ring"></div>

  <div class="abs tag tag-overview">OVERVIEW</div>
  <div class="abs overview-rule"></div>
  <p class="abs overview-text">Torlen Systems provides complete security and<br>technology integration solutions for commercial,<br>industrial, and multifamily properties. From access<br>control to fire systems, we specialize in delivering<br>seamless, scalable,and reliable installations<br>supported by professional service and ongoing care.</p>

  <div class="abs services-panel"></div>
  <div class="abs tag tag-services">SERVICES</div>

  <div class="abs divider" style="left:386px;top:1180px;height:85px"></div>
  <div class="abs divider" style="left:795px;top:1180px;height:85px"></div>
  <div class="abs divider" style="left:386px;top:1400px;height:72px"></div>
  <div class="abs divider" style="left:795px;top:1400px;height:72px"></div>

  <svg class="abs service-icon" style="left:189px;top:1038px" viewBox="0 0 80 80"><path d="M28 34V22a12 12 0 0 1 24 0v12"/><rect x="22" y="34" width="36" height="36" rx="4"/><circle cx="40" cy="50" r="4"/><path d="M40 54v6"/></svg>
  <svg class="abs service-icon" style="left:565px;top:1038px" viewBox="0 0 80 80"><circle cx="40" cy="40" r="32"/><circle cx="40" cy="40" r="16"/><circle cx="40" cy="40" r="7"/><circle cx="40" cy="14" r="3"/><circle cx="40" cy="66" r="3"/><circle cx="14" cy="40" r="3"/><circle cx="66" cy="40" r="3"/><circle cx="22" cy="22" r="3"/><circle cx="58" cy="58" r="3"/><circle cx="58" cy="22" r="3"/><circle cx="22" cy="58" r="3"/></svg>
  <svg class="abs service-icon" style="left:897px;top:1020px;height:92px" viewBox="0 0 80 92"><rect x="8" y="32" width="40" height="56" rx="5"/><rect x="14" y="38" width="28" height="10"/><circle cx="18" cy="58" r="3"/><circle cx="28" cy="58" r="3"/><circle cx="38" cy="58" r="3"/><circle cx="18" cy="68" r="3"/><circle cx="28" cy="68" r="3"/><circle cx="38" cy="68" r="3"/><circle cx="18" cy="78" r="3"/><circle cx="28" cy="78" r="3"/><circle cx="38" cy="78" r="3"/><path d="M44 36c0-14 4-22 12-22s12 8 12 22h-24z"/><path d="M52 40a4 4 0 0 0 8 0"/><path d="M56 8v6"/></svg>
  <svg class="abs service-icon" style="left:158px;top:1285px" viewBox="0 0 80 80"><rect x="4" y="8" width="60" height="44"/><rect x="10" y="14" width="48" height="32"/><path d="M30 40V24l10-3v15"/><circle cx="27" cy="40" r="3"/><path d="M46 62c6-8 22-8 28 0c-6 8-22 8-28 0z"/><circle cx="60" cy="62" r="4"/></svg>
  <svg class="abs service-icon" style="left:560px;top:1278px" viewBox="0 0 80 80"><path d="M40 4c4 14 22 22 22 44a22 22 0 0 1-44 0c0-10 6-16 8-22c2 8 6 10 8 10c0-12 2-22 6-32z"/><path d="M40 44c2 6 10 8 10 18a10 10 0 0 1-20 0c0-6 6-10 10-18z"/></svg>
  <svg class="abs service-icon" style="left:903px;top:1280px" viewBox="0 0 80 80"><rect x="4" y="6" width="72" height="10"/><rect x="4" y="64" width="72" height="10"/><path d="M30 16v48M50 16v48M34 16v48M46 16v48"/><rect x="10" y="20" width="10" height="10"/><rect x="60" y="20" width="10" height="10"/><rect x="10" y="50" width="10" height="10"/><rect x="60" y="50" width="10" height="10"/></svg>

  <section class="abs service" style="left:62px;top:1126px">
    <h3>ACCESS CONTROL :-</h3>
    <p>Cloud-based and enterprise<br>access solutions to manage<br>entry and permissions.</p>
  </section>
  <section class="abs service" style="left:417px;top:1126px">
    <h3>CCTV / VIDEO SURVEILLANCE :-</h3>
    <p>Protect your property with<br>high-definition cameras and<br>remote monitoring.</p>
  </section>
  <section class="abs service" style="left:825px;top:1123px">
    <h3>INTRUSION ALARM :-</h3>
    <p>Professional-grade<br>systems to detect and<br>deter unauthorized access.</p>
  </section>
  <section class="abs service" style="left:62px;top:1369px">
    <h3>AUDIO-VISUAL :-</h3>
    <p>From conference rooms<br>to distributed audio and<br>digital displays.</p>
  </section>
  <section class="abs service" style="left:417px;top:1369px">
    <h3>STRUCTURED DATA CABLING :-</h3>
    <p>Low-voltage and fiber cabling for<br>reliable network infrastructure..</p>
  </section>
  <section class="abs service" style="left:822px;top:1369px">
    <h3>FIRE SYSTEMS :-</h3>
    <p>Code-compliant alarm systems<br>with 24/7 QX monitoring and<br>life-safety support.</p>
  </section>

  <svg class="abs trusted-tail" width="110" height="72" viewBox="0 0 110 72"><polygon points="0,0 62,0 110,71 0,71" fill="#a9d5ea"/><polygon points="0,0 52,0 96,65 0,65" fill="#ffffff"/></svg>
  <div class="abs trusted">
    <span class="label">Trusted By :</span>
    <span class="mark"><span class="dot"></span>MORO</span>
    <span class="mark">Velpurna</span>
    <span class="mark">CARROW</span>
    <span class="mark">QUILLFEN</span>
    <span class="mark">Bolt Hardware</span>
    <span class="mark">LSP</span>
    <span class="mark">KEYframe</span>
  </div>

  <div class="abs tech-bar"></div>
  <p class="abs tech-label">Technology<br>partners :</p>
  <div class="abs partner" style="left:217px;width:151px">Rook Lantern</div>
  <div class="abs partner" style="left:383px;width:143px">Polmira</div>
  <div class="abs partner" style="left:539px;width:143px">Tamzo</div>
  <div class="abs partner" style="left:694px;width:143px">Blazeron<br>by Varnholt</div>
  <div class="abs partner" style="left:853px;width:92px">RTN</div>
  <div class="abs partner" style="left:960px;width:93px;font-size:13px;line-height:15px">Digital<br>Sentrel</div>
  <div class="abs partner" style="left:1068px;width:92px">JMW</div>

  <div class="abs footer"></div>
  <svg class="abs phone-box" width="365" height="62" viewBox="0 0 365 62"><polygon points="38,0 365,0 365,62 0,62" fill="#4da3c9"/></svg>
  <div class="abs footer-brand"><div class="brand-name">TORLEN</div><div class="brand-sub">SYSTEMS</div></div>
  <div class="abs contact" style="left:240px"><svg viewBox="0 0 28 28"><rect x="2" y="6" width="24" height="16"/><path d="M2 6l12 10 12-10"/></svg>sales@torlensystems.example</div>
  <div class="abs contact" style="left:582px"><svg viewBox="0 0 28 28"><circle cx="14" cy="14" r="11"/><path d="M3 14h22M14 3c-5 6-5 16 0 22M14 3c5 6 5 16 0 22"/></svg>torlensystems.example</div>
  <div class="abs phone"><svg viewBox="0 0 24 24"><path d="M6.6 10.8a15 15 0 0 0 6.6 6.6l2.2-2.2a1 1 0 0 1 1-.25 11.4 11.4 0 0 0 3.6.57 1 1 0 0 1 1 1V20a1 1 0 0 1-1 1A17 17 0 0 1 3 4a1 1 0 0 1 1-1h3.5a1 1 0 0 1 1 1c0 1.25.2 2.45.57 3.57a1 1 0 0 1-.25 1z"/></svg>555-014-2739</div>
</main>
</body>
</html>
```